Web Design Project - Wallenbruck Homes

We would like you to refine our web layouts for a (1) homepage and (2) a product page (see attached files for reference).

The client is a swiss construction company, that designs, builds and sells standardized and tailored-made residential houses.

His logo is old, but not up for redesign. The only way to salvage it, is to incorporate its yellow color (as highlight) to the overall design, so as to create some brand awareness.

REQUIREMENTS FOR THE HOMEPAGE:
1. telephone number over menu
2. logo + menu with 6 categories
3. slider for showing various house types (for pics, see attachments)
4. "AKTUELL" card with yellow color (to show his most actual projects) and a strong Call For Action (what in German would be: KONTAKT AUFNEHMEN)
5. a yellow stripe for his company's slogan (Ihr Partner für individuelle und normierte Wohnbauten)
6. A left coloumn with
(a) two picture-holders under the title REFERENZEN
(b) the three supporting logos of TOVU, KALSOTEX and VR KLARWANDBAU VERBUND (can be downloaded as pngs)
7. A right column with 6 headlines + texts of 3 lines each
8. a footer with the adress info

REQUIREMENTS FOR PRODUKT PAGE:
1. slider for pictures
2. info box with Call For Action for particular House-types
3. thumbnail pics under the slider for additional images of any particular house type
4. Left-side: name of house type and picture
5. Right-side: Header and blindtext for house description
6. three placeholders for 3 floor plans

NB No coding necessary. An imaginative, fresh design along the layout requirements will do.
Thanx to all

To all those who had probs with the downloading of the attached files:
we've posted a new Zip.
Have a look!
thankx

Thanks to everyone who participated.
We will be showing a selection of your designs to the client within the next couple of days.
We'll get back to you, as soon as possible.

• - slider
- info box with call for action
- thumbnail pictures
- fresh look based on colors, design of elements (slider, info box), font selection

```html
<!DOCTYPE html>
<html lang="de">
<head>
<meta charset="utf-8">
<title>Wallenbruck Homes</title>
<link rel="stylesheet" href="https://fonts.googleapis.com/css2?family=Arimo:wght@400;700&family=Fira+Sans+Condensed:ital@1&display=swap">
<style>
:root{
  --yellow:#fcc800;
  --yellow-deep:#e8b400;
  --dark:#262626;
  --band:#2c2c2c;
  --panel:#f0f0f0;
  --text:#222;
  --muted:#444;
  --rule:#bdbdbd;
}
*{margin:0;padding:0;box-sizing:border-box}
html,body{width:1200px;height:1200px;overflow:hidden;background:#fff}
body{position:relative;font-family:"Arimo",Arial,sans-serif;color:var(--text)}
.abs{position:absolute}

.brand{left:152px;top:38px;display:flex;align-items:center;gap:8px;font-weight:700;font-size:17px;color:#111}
.brand-mark{width:14px;height:14px;background:var(--yellow)}

.main-nav{left:500px;top:58px;width:552px;height:22px;border-bottom:3px solid #e6e6e6;display:flex;justify-content:space-between;font-weight:700;font-size:12.5px;letter-spacing:.2px}
.main-nav a{color:#111;text-decoration:none;height:22px}
.main-nav a.active{color:#888;border-bottom:3px solid var(--yellow)}

.dark-band{left:0;top:100px;width:1200px;height:260px;background:var(--band)}
.hero-card{left:120px;top:120px;width:960px;height:272px;background:#fff;border-radius:8px}
.slider{left:130px;top:130px;width:450px;height:250px}
.slider-photo{width:450px;height:220px;background:linear-gradient(180deg,#3b57b8 0%,#6d86d4 45%,#d9d6cf 62%,#6f7b55 100%)}
.slider-bar{height:30px;background:#1e1e1e;display:flex;align-items:center;gap:6px;padding-left:20px}
.dot{width:8px;height:8px;background:#fff}
.dot.on{background:var(--yellow)}

.news{left:580px;top:130px;width:490px;height:250px;background:var(--panel)}
.news h2{position:absolute;left:61px;top:27px;font-size:16px;font-weight:700;letter-spacing:.5px}
.news .h-rule{position:absolute;left:150px;top:38px;width:280px;height:3px;background:#222}
.news ul{position:absolute;left:150px;top:56px;width:285px;list-style:none}
.news li{height:27px;border-bottom:1px dotted var(--rule);display:flex;align-items:center;gap:8px;font-size:14px;color:#333}
.news svg{flex:none}
.cta{position:absolute;left:149px;top:204px;width:162px;height:31px;border-radius:4px;background:linear-gradient(#f4f4f4,#cfcfcf);border:1px solid #c4c4c4;font-weight:700;font-size:12px;color:#333;display:flex;align-items:center;justify-content:center}

.slogan{left:120px;top:385px;width:960px;height:48px;background:var(--yellow);font-family:"Fira Sans Condensed",sans-serif;font-style:italic;font-size:19px;color:#3a2f00;padding:13px 0 0 30px;letter-spacing:.3px}
.slogan-cap{left:120px;top:430px;width:960px;height:10px;background:#fff;border-radius:8px 8px 0 0}

.side-title{left:128px;top:447px;font-size:18px}
.ref{left:130px;width:290px;height:180px}
.ref-head{height:30px;background:var(--yellow-deep);color:#fff;font-weight:700;font-size:13px;padding:8px 10px;border-radius:6px 6px 0 0}
.ref-photo{height:150px;border-radius:0 30px 0 0;margin-top:-0px}
.ref-photo.one{background:linear-gradient(180deg,#3c55b3 0%,#8aa0dc 45%,#e3e1db 70%,#77805d 100%)}
.ref-photo.two{background:linear-gradient(180deg,#b8c8e0 0%,#e9edf2 50%,#d8d8d4 80%,#8a8f86 100%)}

.partner{left:130px;display:flex;align-items:center;gap:8px;font-weight:700;color:#222}
.partner-box{width:30px;height:30px;flex:none}

.content{left:450px;top:447px;width:612px}
.content h3{font-size:18px;font-weight:400;margin-bottom:4px;color:#111}
.content p{font-size:12px;line-height:14.5px;color:var(--muted);margin-bottom:10px;height:55px}

.footer{left:130px;top:1100px;width:940px;height:60px;background:var(--dark);border-radius:8px;color:#eee;font-size:12.5px}
.footer div{position:absolute;top:10px;line-height:21px}
.copyright{right:140px;top:1167px;font-size:11px;color:#333}
</style>
</head>
<body>

<div class="abs brand"><span class="brand-mark"></span>Wallenbruck Homes</div>

<nav class="abs main-nav">
  <a class="active">HOME</a><a>HÄUSER</a><a>RENOVATIONEN</a><a>REFERENZEN</a><a>ÜBER UNS</a><a>KONTAKT</a>
</nav>

<div class="abs dark-band"></div>
<div class="abs hero-card"></div>

<div class="abs slider">
  <div class="slider-photo" role="img" aria-label="Foto eines weissen Einfamilienhauses mit Ziegeldach unter blauem Himmel"></div>
  <div class="slider-bar">
    <svg width="10" height="14" viewBox="0 0 10 14"><path d="M8 1 2 7l6 6" fill="none" stroke="#fff" stroke-width="2.5"/></svg>
    <span class="dot on"></span><span class="dot"></span><span class="dot"></span><span class="dot"></span><span class="dot"></span>
    <svg width="10" height="14" viewBox="0 0 10 14"><path d="M2 1l6 6-6 6" fill="none" stroke="#fff" stroke-width="2.5"/></svg>
  </div>
</div>

<section class="abs news">
  <h2>AKTUELL</h2><span class="h-rule"></span>
  <ul>
    <li><svg width="14" height="14" viewBox="0 0 14 14"><path d="M7 1 13 7 7 13 1 7Z" fill="none" stroke="#f0b800" stroke-width="1.5"/><path d="M5 7h4M7 5l2 2-2 2" stroke="#f0b800" fill="none"/></svg>Bauland in Itaslen, TG</li>
    <li><svg width="14" height="14" viewBox="0 0 14 14"><path d="M7 1 13 7 7 13 1 7Z" fill="none" stroke="#f0b800" stroke-width="1.5"/><path d="M5 7h4M7 5l2 2-2 2" stroke="#f0b800" fill="none"/></svg>Bauland in Sirnach, TG</li>
    <li><svg width="14" height="14" viewBox="0 0 14 14"><path d="M7 1 13 7 7 13 1 7Z" fill="none" stroke="#f0b800" stroke-width="1.5"/><path d="M5 7h4M7 5l2 2-2 2" stroke="#f0b800" fill="none"/></svg>EFN in Balterswill, TG</li>
    <li><svg width="14" height="14" viewBox="0 0 14 14"><path d="M7 1 13 7 7 13 1 7Z" fill="none" stroke="#f0b800" stroke-width="1.5"/><path d="M5 7h4M7 5l2 2-2 2" stroke="#f0b800" fill="none"/></svg>EFN in Münchwilen, TG</li>
    <li><svg width="14" height="14" viewBox="0 0 14 14"><path d="M7 1 13 7 7 13 1 7Z" fill="none" stroke="#f0b800" stroke-width="1.5"/><path d="M5 7h4M7 5l2 2-2 2" stroke="#f0b800" fill="none"/></svg>Wohnungen in Eschlikon, TG</li>
  </ul>
  <div class="cta">KONTAKT AUFNEHMEN</div>
</section>

<div class="abs slogan">Ihr Partner für individuelle und normierte Wohnbauten</div>
<div class="abs slogan-cap"></div>

<h2 class="abs side-title" style="font-weight:400">Referenzen</h2>

<div class="abs ref" style="top:477px">
  <div class="ref-head">Titel des Bildes ein</div>
  <div class="ref-photo one" role="img" aria-label="Foto eines weissen Hauses mit Garten"></div>
</div>
<div class="abs ref" style="top:677px">
  <div class="ref-head">Titel des Bildes zwei</div>
  <div class="ref-photo two" role="img" aria-label="Foto eines weissen Hauses mit Balkon"></div>
</div>

<div class="abs partner" style="top:893px;font-size:20px"><span class="partner-box" style="background:#3a9a5a"></span>TOVU</div>
<div class="abs partner" style="top:965px;font-size:24px"><span class="partner-box" style="background:#d42020"></span>KALSOTEX</div>
<div class="abs partner" style="top:1020px;font-size:13px"><span class="partner-box" style="background:#b02020;width:24px;height:24px"></span>VR KLARWANDBAU VERBUND</div>

<main class="abs content">
  <h3>Beratung und Betreuung</h3>
  <p>Lorem ipsum dolor sit amet, consectetur adipiscing elit. Vestibulum sed convallis metus. Proin pulvinar, tortor eget gravida faucibus, justo enim tempor lacus, ut ultricies nibh nisi vel lectus. Vivamus quis justo dolor, sit amet ultrices turpis.</p>
  <h3>Auf Ihre Wünsche</h3>
  <p>Aenean convallis lorem metus. Integer a eros vitae nisi rhoncus aliquet. Sed pellentesque eleifend erat, id pellentesque sem lobortis vitae. Aliquam erat volutpat. Nunc hendrerit nunc tortor. In sodales nisi non tortor sagittis luctus. Nullam commodo lobortis ante, vel auctor urna facilisis quis.</p>
  <h3>Zusammenarbeit</h3>
  <p>Maecenas pharetra nunc dui. Donec lacinia elit non nisi sodales eleifend. Donec vehicula, nisi quis tincidunt consectetur, metus sapien volutpat ante, vitae blandit arcu urna sit amet ligula. Nunc condimentum, lectus rhoncus viverra sollicitudin, nulla quam sagittis purus, non rutrum lorem sapien sit amet eros.</p>
  <h3>Für jedes Bugdet</h3>
  <p>Vivamus sodales orci nec nulla pharetra volutpat. Fusce libero neque, sagittis vel pharetra eget, viverra a nibh. Praesent mauris lectus, mollis id elementum eu, sollicitudin in arcu. Nulla lacinia tortor nec elit euismod a malesuada purus molestie. Aenean id sem libero, et eleifend sapien.</p>
  <h3>Umweltfreundlich</h3>
  <p>Aliquam volutpat massa quis turpis malesuada interdum. Donec pulvinar ligula in erat fringilla condimentum. Etiam vitae quam ipsum, ac pretium purus. Cum sociis natoque penatibus et magnis dis parturient montes, nascetur ridiculus mus. Sed nec egestas massa. Vivamus euismod aliquam commodo.</p>
  <h3>Kundenzufriedenheit</h3>
  <p>Lorem ipsum dolor sit amet, consectetur adipiscing elit. Vestibulum sed convallis metus. Proin pulvinar, tortor eget gravida faucibus, justo enim tempor lacus, ut ultricies nibh nisi vel lectus. Vivamus quis justo dolor, sit amet ultrices turpis. Donec ante enim, gravida vel pharetra vitae, volutpat in urna.</p>
</main>

<footer class="abs footer">
  <div style="left:30px">Wallenbruck Wohnbauten GmbH<br>Fam. Brändli</div>
  <div style="left:240px">Talackerweg 14<br>CH-8374 Oberwangen</div>
  <div style="left:480px">Tel. 071 555 01 20<br>Fax. 071 555 01 21</div>
  <div style="left:720px">info@wallenbruck-homes.ch</div>
</footer>
<div class="abs copyright">All contents © copyright 1999-2013 Wallenbruck Wohnbauten GmbH. All rights reserved.</div>

</body>
</html>
```